Brochure design for garden shed range for www.yardhuts2go.ie

we want to have a brochure designed for our products at www.yardhuts2go.ie
this should clearly show the ranges of products we sell and there features it wont need all our pricing but more to show our quality of products. We can work together with designers to get the right information on all our ranges and any text needed for the brochure.

Target Market(s)

general public

Industry/Entity Type

Home And Garden

```html
<!DOCTYPE html>
<html lang="en">
<head>
<meta charset="utf-8">
<title>Yardhuts2go Brochure</title>
<link href="https://fonts.googleapis.com/css2?family=Oswald:wght@500;600;700&family=Arimo:wght@400&display=swap" rel="stylesheet">
<style>
:root{
  --forest:#173d17;
  --heading:#3b4a1c;
  --olive:#6a6a24;
  --orange:#c97a2b;
  --badge:#3f9a2f;
  --badge-light:#7cc24a;
  --ink:#555;
  --white:#fff;
}
*{margin:0;padding:0;box-sizing:border-box}
html,body{width:1200px;height:928px;overflow:hidden;background:#fff}
.page{position:relative;width:1200px;height:928px;overflow:hidden;
  background:linear-gradient(#e6e6e6 0,#fff 40px);font-family:'Oswald',sans-serif}
.abs{position:absolute}
.decor{position:absolute;left:0;top:0}
.title{position:absolute;font-weight:700;color:var(--heading);text-transform:uppercase;line-height:1;white-space:nowrap}
.title span{color:var(--orange)}
.range-title{font-size:25px}
.model-title{font-size:20px;font-weight:600}
.photo{position:absolute;border:4px solid #fff;box-shadow:0 2px 6px rgba(0,0,0,.35)}
.photo.warm{background:linear-gradient(160deg,#b58250,#8a5a2f 60%,#6c4a2a)}
.photo.pale{background:linear-gradient(160deg,#b9b8a4,#d8d2b8 55%,#9a9a86)}
.badge{position:absolute;width:132px;height:132px;border-radius:50%;
  background:radial-gradient(circle at 45% 35%,var(--badge-light),var(--badge) 55%,#226b1c);
  border:3px solid #fff;box-shadow:0 3px 8px rgba(0,0,0,.4);
  display:flex;flex-direction:column;align-items:center;justify-content:center;color:#fff;text-transform:uppercase;line-height:1.05}
.badge .from{font-size:19px;font-weight:600}
.badge .price{font-size:33px;font-weight:700}
.welcome{position:absolute;left:804px;top:32px;font-weight:700;color:var(--heading);line-height:1}
.welcome .l1{font-size:40px}
.welcome .l2{font-size:50px;margin-top:6px}
.welcome .l2 span{color:var(--orange)}
.point{position:absolute;left:900px;width:258px;font-family:'Arimo',sans-serif;font-size:14.4px;line-height:19px;color:var(--ink);text-align:justify}
.numeral{position:absolute;width:62px;height:62px;border-radius:50%;background:var(--orange);color:#fff;
  font-size:52px;font-weight:700;display:flex;align-items:center;justify-content:center;line-height:1}
.band{position:absolute;left:0;width:1200px}
.band.olive{top:546px;height:50px;background:var(--olive)}
.band.forest{top:596px;height:332px;background:var(--forest)}
.band-title{position:absolute;top:552px;font-size:30px;font-weight:600;color:#fff;text-transform:uppercase;line-height:1}
.band-title span{color:var(--orange)}
.thumb{position:absolute;width:136px;height:136px;border-radius:50%;border:3px solid #fff;box-shadow:0 0 0 3px #2d6a2a}
.thumb.warm{background:radial-gradient(circle at 50% 40%,#b98552,#7a5330 70%,#4c6b3c)}
.thumb.pale{background:radial-gradient(circle at 50% 40%,#d7d2bb,#a9a690 70%,#6b7a5a)}
.item{position:absolute;text-transform:uppercase;line-height:1.2;font-weight:600}
.item .name{color:#fff;font-size:22px}
.item .price{color:var(--orange);font-size:22px}
</style>
</head>
<body>
<div class="page">

  <svg class="decor" width="1200" height="600" viewBox="0 0 1200 600" aria-hidden="true">
    <path d="M0 470 L420 340 L420 380 L0 520 Z" fill="#2f5a1f"/>
    <path d="M0 520 L420 380 L420 400 L0 540 Z" fill="var(--orange)"/>
    <path d="M400 420 L760 300 L760 330 L400 440 Z" fill="#2f5a1f"/>
    <path d="M400 440 L760 330 L760 345 L400 455 Z" fill="var(--orange)"/>
    <path d="M774 232 C900 160 1050 125 1200 110 L1200 150 C1060 160 920 190 774 232 Z" fill="var(--heading)"/>
    <path d="M774 232 C920 200 1060 175 1200 168 L1200 196 C1060 198 920 215 774 240 Z" fill="#3f7a2a"/>
    <path d="M774 268 C920 225 1060 208 1200 205 L1200 238 C1060 236 920 245 774 268 Z" fill="var(--orange)"/>
  </svg>

  <div class="title range-title" style="left:54px;top:42px">Premium <span>Sheds</span></div>
  <div class="title model-title" style="left:54px;top:86px">Premium <span>Standard</span></div>
  <div class="photo warm" style="left:58px;top:116px;width:340px;height:188px" role="img" aria-label="Photo of a premium standard timber garden shed"></div>
  <div class="badge" style="left:264px;top:78px"><span class="from">Range from</span><span class="price">€399.99</span></div>

  <div class="title model-title" style="left:54px;top:318px">Premium <span>Kendal</span></div>
  <div class="photo warm" style="left:58px;top:350px;width:340px;height:188px" role="img" aria-label="Photo of a premium Kendal shed with windows"></div>
  <div class="badge" style="left:264px;top:294px"><span class="from">Range from</span><span class="price">€579.99</span></div>

  <div class="title range-title" style="left:428px;top:42px">Overlap <span>Sheds</span></div>
  <div class="title model-title" style="left:428px;top:86px">Overlap <span>Lean</span></div>
  <div class="photo pale" style="left:432px;top:116px;width:326px;height:188px" role="img" aria-label="Photo of an overlap lean-to shed"></div>
  <div class="badge" style="left:636px;top:78px"><span class="from">Range from</span><span class="price">€339.00</span></div>

  <div class="title model-title" style="left:428px;top:318px">Overlap <span>Standard</span></div>
  <div class="photo pale" style="left:432px;top:350px;width:326px;height:188px" role="img" aria-label="Photo of an overlap standard shed"></div>
  <div class="badge" style="left:636px;top:294px"><span class="from">Range from</span><span class="price">€399.99</span></div>

  <div class="welcome">
    <div class="l1">WELCOME TO</div>
    <div class="l2">IRELAND'S <span>NO.1</span></div>
  </div>

  <div class="numeral" style="left:814px;top:264px">1</div>
  <p class="point" style="top:282px">At yardhuts2go.ie we take great pride in supplying quality garden sheds to our customers troughout Ireland All of our sheds are manafactured and treated inhouse.</p>
  <div class="numeral" style="left:814px;top:408px">2</div>
  <p class="point" style="top:404px">We only source material from European certified stockist and work closely with our suppliers to ensure the quality of our timber before it is used to manafacture our range of products.</p>

  <div class="band olive"></div>
  <div class="band forest"></div>
  <div class="band-title" style="left:54px">Kendal <span>Sheds</span></div>
  <div class="band-title" style="left:422px">Lean to <span>Sheds</span></div>
  <div class="band-title" style="left:804px">Kids <span>Sheds</span></div>

  <div class="thumb warm" style="left:52px;top:606px" role="img" aria-label="Premium Kendal shed photo"></div>
  <div class="item" style="left:206px;top:640px"><div class="name">Premium Kendal</div><div class="price">Range from €579.99</div></div>
  <div class="thumb pale" style="left:52px;top:768px" role="img" aria-label="Overlap Kendal shed photo"></div>
  <div class="item" style="left:206px;top:806px"><div class="name">Overlap Kendal</div><div class="price">Range from €479.99</div></div>

  <div class="thumb warm" style="left:430px;top:606px" role="img" aria-label="Premium lean-to shed photo"></div>
  <div class="item" style="left:584px;top:640px"><div class="name">Premium Lean</div><div class="price">To from €349.99</div></div>
  <div class="thumb pale" style="left:430px;top:768px" role="img" aria-label="Overlap lean-to shed photo"></div>
  <div class="item" style="left:584px;top:806px"><div class="name">Overlap Lean</div><div class="price">Range from €339.00</div></div>

  <div class="thumb warm" style="left:808px;top:606px" role="img" aria-label="Kids playhouse photo"></div>
  <div class="item" style="left:962px;top:640px"><div class="name">Kids Playhouse</div><div class="price">Range from €449.99</div></div>
  <div class="thumb warm" style="left:808px;top:768px" role="img" aria-label="Kids tree house photo"></div>
  <div class="item" style="left:962px;top:806px"><div class="name">Kids Tree House</div><div class="price">Range from €799.99</div></div>

</div>
</body>
</html>
```